Tallowbrook Aesthetic Medic is the title and the name of the business

Chatterleaf advertising: keep
To those dimensions

Aimed at Caucasian women between the ages of 18 - 60 interested in beauty and cosmetic injectables. Will be boosted on chatterleaf which is my advertising platform.

Name: Tallowbrook Aesthetic Medic
0491 570 318

Forehead $58
Frown lines $116
Crows feet $116
Lip fillers $380

I would like to have a beautiful girl that suits the picture.

Target Market(s)

Females between 18 - 60 interested in Lumiset and cosmetic fillers
Prefer Caucasian as that's the majority of population

Industry/Entity Type

Beauty Salon

Font styles to use
Serif
Script

Colors
e667a6
eea4c8
f9d9e8
fee18a
fbf289
fbee3d
cadf82
cedeed
85cae6

Requirements
Must have
• Name: Tallowbrook Aesthetic Medic
• Phone number: 0491 570 381
• Prices:
• Forehead $58
• Frown lines $116
• Crows feet $116
• Lip fillers $380
• Picture of female that is very beautiful
Nice to have
• Not a cartoon or anything else that's not a real picture of a female
Should not have
• No cartoon pictures. Proper picture of women

```html
<!DOCTYPE html>
<html lang="en">
<head>
<meta charset="utf-8">
<title>Tallowbrook Aesthetic Medic – Ad Set</title>
<link rel="stylesheet" href="https://fonts.googleapis.com/css2?family=Cabin:wght@400;700&family=Cinzel:wght@400;600&family=Tenor+Sans&display=swap">
<style>
  :root {
    --page: #ebebeb;
    --label-ink: #1c1c1c;
    --ad-bg: #2e2b2e;
    --ad-bg-deep: #1f1d20;
    --ad-swirl: #3a373b;
    --ad-text: #f4ede6;
    --tile-frame: #141214;
    --tile-face: #fcefe2;
    --tile-ink: #4a2323;
    --tile-rule: #6e3f3f;
    --hair: #3b2a24;
    --skin: #e6c0aa;
    --skin-light: #f1d6c6;
    --lip: #c4161c;
  }
  * { box-sizing: border-box; margin: 0; padding: 0; }
  html, body { width: 1200px; height: 1200px; overflow: hidden; }
  body { background: var(--page); position: relative; font-family: "Cinzel", serif; }

  .size-label {
    position: absolute; transform: translate(-50%, -50%);
    font-family: "Cabin", sans-serif; font-size: 22px; color: var(--label-ink);
    white-space: nowrap;
  }
  .size-label--tall { left: 308px; top: 110px; }
  .size-label--square-l { left: 853px; top: 149px; }
  .size-label--square-s { left: 853px; top: 727px; }

  .ad {
    position: absolute; overflow: hidden; color: var(--ad-text);
    background:
      radial-gradient(circle at 12% 30%, var(--ad-swirl) 0, transparent 38%),
      radial-gradient(circle at 20% 90%, var(--ad-swirl) 0, transparent 30%),
      linear-gradient(180deg, var(--ad-bg) 0%, var(--ad-bg-deep) 100%);
    box-shadow: 3px 4px 6px rgba(0,0,0,.35);
  }
  .ad--tall { left: 108px; top: 138px; width: 403px; height: 960px; }
  .ad--square-l { left: 613px; top: 176px; width: 480px; height: 480px; }
  .ad--square-s { left: 692px; top: 751px; width: 322px; height: 321px; }

  .ad__photo { position: absolute; }
  .ad--tall .ad__photo {
    left: 0; top: 102px; width: 100%; height: 358px;
    background:
      radial-gradient(ellipse 22% 30% at 64% 45%, var(--skin-light) 0, var(--skin) 60%, transparent 100%),
      radial-gradient(ellipse 34% 55% at 65% 55%, var(--hair) 0, transparent 100%),
      linear-gradient(90deg, #3a383b 0%, #5a5558 100%);
  }
  .ad--square-l .ad__photo {
    right: 0; top: 0; width: 250px; height: 100%;
    background:
      radial-gradient(ellipse 38% 40% at 62% 40%, var(--skin-light) 0, var(--skin) 60%, transparent 100%),
      radial-gradient(ellipse 60% 70% at 65% 45%, var(--hair) 0, transparent 100%),
      linear-gradient(90deg, transparent 0%, rgba(60,55,58,.6) 40%);
  }
  .ad--square-s .ad__photo {
    right: 0; top: 0; width: 170px; height: 100%;
    background:
      radial-gradient(ellipse 38% 40% at 62% 40%, var(--skin-light) 0, var(--skin) 60%, transparent 100%),
      radial-gradient(ellipse 60% 70% at 65% 45%, var(--hair) 0, transparent 100%),
      linear-gradient(90deg, transparent 0%, rgba(60,55,58,.6) 40%);
  }

  .ad__title {
    position: absolute; text-align: center; font-weight: 400;
    line-height: 1.15; letter-spacing: .02em; text-shadow: 0 1px 2px rgba(0,0,0,.5);
  }
  .ad--tall .ad__title { left: 0; width: 100%; top: 20px; font-size: 26px; }
  .ad--square-l .ad__title { left: 0; width: 340px; top: 28px; font-size: 22px; }
  .ad--square-s .ad__title { left: 0; width: 224px; top: 17px; font-size: 15px; }

  .ad__intro { position: absolute; text-align: center; line-height: 1.3; }
  .ad--tall .ad__intro { left: 30px; width: 343px; top: 474px; font-size: 13px; }
  .ad--tall .ad__intro p + p { margin-top: 8px; }
  .ad--square-l .ad__intro { left: 0; width: 340px; top: 107px; font-size: 10px; }
  .ad--square-s .ad__intro { left: 0; width: 224px; top: 56px; font-size: 8px; }

  .ad__prices-heading { position: absolute; text-align: center; }
  .ad--tall .ad__prices-heading { left: 0; width: 100%; top: 561px; font-size: 13px; }
  .ad--square-l .ad__prices-heading { left: 0; width: 340px; top: 137px; font-size: 10px; }
  .ad--square-s .ad__prices-heading { left: 0; width: 224px; top: 85px; font-size: 8px; }

  .price-grid {
    position: absolute; display: grid;
    grid-template-columns: 1fr 1fr; grid-template-rows: 1fr 1fr;
  }
  .ad--tall .price-grid { left: 40px; top: 590px; width: 320px; height: 298px; gap: 17px 18px; --label: 16px; --price: 40px; --notch: 10px; }
  .ad--square-l .price-grid { left: 30px; top: 157px; width: 274px; height: 252px; gap: 12px 14px; --label: 13px; --price: 34px; --notch: 9px; }
  .ad--square-s .price-grid { left: 20px; top: 106px; width: 182px; height: 163px; gap: 12px 13px; --label: 9px; --price: 22px; --notch: 6px; }

  .price-tile {
    --cut: polygon(var(--notch) 0, calc(100% - var(--notch)) 0, 100% var(--notch), 100% calc(100% - var(--notch)), calc(100% - var(--notch)) 100%, var(--notch) 100%, 0 calc(100% - var(--notch)), 0 var(--notch));
    background: var(--tile-frame); clip-path: var(--cut); padding: 3px;
  }
  .price-tile__face {
    height: 100%; background: var(--tile-face); clip-path: var(--cut);
    display: flex; flex-direction: column; align-items: center; justify-content: center;
    color: var(--tile-ink);
  }
  .price-tile__name {
    font-family: "Tenor Sans", sans-serif; font-size: var(--label);
    border-bottom: 3px double var(--tile-rule); padding: 0 4px 2px; margin-bottom: 4px;
  }
  .price-tile__price { font-family: "Cabin", sans-serif; font-weight: 700; font-size: var(--price); line-height: 1.1; }

  .ad__phone { position: absolute; text-align: center; font-family: "Tenor Sans", sans-serif; transform: translateY(-50%); }
  .ad__address { position: absolute; text-align: center; transform: translateY(-50%); }
  .ad--tall .ad__phone { left: 0; width: 100%; top: 913px; font-size: 24px; }
  .ad--tall .ad__address { left: 0; width: 100%; top: 936px; font-size: 11px; }
  .ad--square-l .ad__phone { left: 0; width: 334px; top: 432px; font-size: 22px; }
  .ad--square-l .ad__address { left: 0; width: 334px; top: 454px; font-size: 11px; }
  .ad--square-s .ad__phone { left: 0; width: 222px; top: 286px; font-size: 12px; }
  .ad--square-s .ad__address { left: 0; width: 222px; top: 302px; font-size: 8px; }
</style>
</head>
<body>

  <div class="size-label size-label--tall">504 x 1200</div>
  <div class="size-label size-label--square-l">600 x 600</div>
  <div class="size-label size-label--square-s">400 x 400</div>

  <!-- Tall banner -->
  <section class="ad ad--tall">
    <div class="ad__photo" role="img" aria-label="Photo of a dark-haired woman with red lips and red nails, hand raised to her chin"></div>
    <h1 class="ad__title">Tallowbrook Aesthetic<br>Medic</h1>
    <div class="ad__intro">
      <p>We only use premium products from Veloria,</p>
      <p>offering a free consultation with a doctor</p>
    </div>
    <div class="ad__prices-heading">Prices:</div>
    <div class="price-grid">
      <div class="price-tile"><div class="price-tile__face"><span class="price-tile__name">Forehead</span><span class="price-tile__price">$58</span></div></div>
      <div class="price-tile"><div class="price-tile__face"><span class="price-tile__name">Frown lines</span><span class="price-tile__price">$116</span></div></div>
      <div class="price-tile"><div class="price-tile__face"><span class="price-tile__name">Crows feet</span><span class="price-tile__price">$116</span></div></div>
      <div class="price-tile"><div class="price-tile__face"><span class="price-tile__name">Lip fillers</span><span class="price-tile__price">$380</span></div></div>
    </div>
    <div class="ad__phone">0491 570 318</div>
    <div class="ad__address">41 Harrow Vale Eastbury</div>
  </section>

  <!-- 600 square -->
  <section class="ad ad--square-l">
    <div class="ad__photo" role="img" aria-label="Photo of a dark-haired woman with red lips and red nails, hand raised to her chin"></div>
    <h1 class="ad__title">Tallowbrook Aesthetic<br>Medic</h1>
    <div class="ad__intro">
      <p>We only use premium products from Veloria,</p>
      <p>offering a free consultation with a doctor</p>
    </div>
    <div class="ad__prices-heading">Prices:</div>
    <div class="price-grid">
      <div class="price-tile"><div class="price-tile__face"><span class="price-tile__name">Forehead</span><span class="price-tile__price">$58</span></div></div>
      <div class="price-tile"><div class="price-tile__face"><span class="price-tile__name">Frown lines</span><span class="price-tile__price">$116</span></div></div>
      <div class="price-tile"><div class="price-tile__face"><span class="price-tile__name">Crows feet</span><span class="price-tile__price">$116</span></div></div>
      <div class="price-tile"><div class="price-tile__face"><span class="price-tile__name">Lip fillers</span><span class="price-tile__price">$380</span></div></div>
    </div>
    <div class="ad__phone">0491 570 318</div>
    <div class="ad__address">41 Harrow Vale Eastbury</div>
  </section>

  <!-- 400 square -->
  <section class="ad ad--square-s">
    <div class="ad__photo" role="img" aria-label="Photo of a dark-haired woman with red lips and red nails, hand raised to her chin"></div>
    <h1 class="ad__title">Tallowbrook Aesthetic<br>Medic</h1>
    <div class="ad__intro">
      <p>Premium products from Veloria.</p>
      <p>Free consultation with a doctor.</p>
    </div>
    <div class="ad__prices-heading">Prices:</div>
    <div class="price-grid">
      <div class="price-tile"><div class="price-tile__face"><span class="price-tile__name">Forehead</span><span class="price-tile__price">$58</span></div></div>
      <div class="price-tile"><div class="price-tile__face"><span class="price-tile__name">Frown lines</span><span class="price-tile__price">$116</span></div></div>
      <div class="price-tile"><div class="price-tile__face"><span class="price-tile__name">Crows feet</span><span class="price-tile__price">$116</span></div></div>
      <div class="price-tile"><div class="price-tile__face"><span class="price-tile__name">Lip fillers</span><span class="price-tile__price">$380</span></div></div>
    </div>
    <div class="ad__phone">0491 570 318</div>
    <div class="ad__address">41 Harrow Vale Eastbury</div>
  </section>

</body>
</html>
```